Birchby Candles, Hand-poured scented soy candles

Create a logo and label design to use on my vintage country farmhouse style, all natural, hand poured soy candle jars and apothecaries. Candles will be labeled in 4 different sizes so design must be adaptable, clean, simple, telegraphic and invoke interest in the product. Think Black lettering on white or black on kraft brown. 603 is the area code for New Hampshire where we make them. The labels will need a prominent area for the scent of the candle to be listed that the eyes are drawn to. Primitive country in design? Use of state attractions? Jars are a square mason style 8 ounce and 16 ounce. Tarts are a clamshell. Lids are a 70-400 series 2.5" label area. Candles are white in a clear glass jar, black lids. There will be label design sizes of 3"x 2.5" 2.5" round, 1.5"x2.5"

Target Market(s)

primitive country, farmhouse, vintage, general home decor

Contact Information for Business Card

Birchby Candles, all natural soy candles, hand-poured in New Hampshire, logo, phone, address. Possibly match the main label.

Logo Text

Birchby Candles, all natural soy candles, hand-poured in New Hampshire, area for scent description and size of container.

Font styles to use
Serif
Script

Colors

Designer to choose colors to be used in the design.

Requirements
Must have
• simple and clean, country farmhouse with a bit of vintage thrown in. possibly multiple fonts to distinguish info from scent name
Nice to have
• at this time I am open to suggestions
• Prefer scent names or brand name in an older script?
• older copperplate/Spencerian?
Should not have
• cluttered, busy, too modern, multiple colors

```html
<!DOCTYPE html>
<html lang="en">
<head>
<meta charset="utf-8">
<title>Birchby Candles — Soy Candle Label</title>
<link rel="stylesheet" href="https://fonts.googleapis.com/css2?family=Playfair+Display:wght@400;700&family=Parisienne&display=swap">
<style>
  :root {
    --page: #f4efe9;
    --label: #f7b98b;
    --label-light: #fac8a2;
    --ink: #232838;
    --ink-soft: rgba(35, 40, 56, 0.3);
  }
  * { margin: 0; padding: 0; box-sizing: border-box; }
  html, body {
    width: 929px;
    height: 1200px;
    overflow: hidden;
    background: var(--page);
  }
  .canvas {
    position: relative;
    width: 929px;
    height: 1200px;
  }
  .label {
    position: absolute;
    left: 120px;
    top: 234px;
    width: 708px;
    height: 606px;
    background: linear-gradient(100deg, var(--label) 0%, var(--label-light) 55%, var(--label) 100%);
    color: var(--ink);
  }
  .label > * { position: absolute; }
  .origin-arc {
    left: 0;
    top: 0;
    width: 708px;
    height: 250px;
  }
  .origin-arc text {
    font-family: "Playfair Display", serif;
    font-size: 16px;
    letter-spacing: 1px;
    fill: var(--ink);
  }
  .brand-name {
    left: 0;
    width: 100%;
    top: 150px;
    font-family: "Playfair Display", serif;
    font-weight: 400;
    font-size: 66px;
    line-height: 1.05;
    letter-spacing: 3px;
    text-align: center;
  }
  .flourish {
    height: 10px;
    border-radius: 5px;
    background: var(--ink-soft);
  }
  .flourish--upper-left { left: 154px; top: 367px; width: 140px; }
  .flourish--upper-right { left: 420px; top: 367px; width: 138px; }
  .flourish--lower-left { left: 170px; top: 571px; width: 140px; }
  .flourish--lower-right { left: 400px; top: 571px; width: 140px; }
  .tagline, .product {
    left: 0;
    width: 100%;
    text-align: center;
    font-family: "Playfair Display", serif;
    font-weight: 700;
    text-transform: uppercase;
    line-height: 1;
    transform: scaleX(0.76);
  }
  .tagline {
    top: 390px;
    font-size: 48px;
    letter-spacing: 2px;
  }
  .product {
    top: 437px;
    font-size: 70px;
    letter-spacing: 2px;
  }
  .rule {
    height: 2px;
    background: var(--ink);
  }
  .rule--top { left: 180px; width: 348px; top: 507px; }
  .rule--bottom { left: 156px; width: 382px; top: 550px; }
  .scent {
    left: 0;
    width: 100%;
    top: 510px;
    text-align: center;
    font-family: "Parisienne", cursive;
    font-size: 36px;
    line-height: 1.1;
  }
  .size {
    left: 0;
    width: 100%;
    top: 561px;
    text-align: center;
    font-family: "Playfair Display", serif;
    font-weight: 700;
    font-size: 28px;
    line-height: 1;
  }
</style>
</head>
<body>
<main class="canvas">
  <section class="label" aria-label="Birchby Candles soy candle label">
    <svg class="origin-arc" viewBox="0 0 708 250" aria-label="Hand-poured in New Hampshire">
      <defs>
        <path id="origin-curve" d="M 196 210 A 158 158 0 0 1 512 210" fill="none"/>
      </defs>
      <text text-anchor="middle">
        <textPath href="#origin-curve" startOffset="50%">HAND-POURED IN NEW HAMPSHIRE</textPath>
      </text>
    </svg>

    <h1 class="brand-name">Birchby<br>Candles</h1>

    <div class="flourish flourish--upper-left" role="img" aria-label="Decorative scroll flourish"></div>
    <div class="flourish flourish--upper-right" role="img" aria-label="Decorative scroll flourish"></div>

    <p class="tagline">All Natural</p>
    <h2 class="product">Soy Candles</h2>

    <div class="rule rule--top"></div>
    <p class="scent">Lavender&amp; Chamomille</p>
    <div class="rule rule--bottom"></div>

    <div class="flourish flourish--lower-left" role="img" aria-label="Decorative scroll flourish"></div>
    <p class="size">8 oz</p>
    <div class="flourish flourish--lower-right" role="img" aria-label="Decorative scroll flourish"></div>
  </section>
</main>
</body>
</html>
```